Website Refresh of tvga-tl.com

INTRODUCTION: The Tolvane Valley Growth Alliance (TVGA) is a 501-C3 nonprofit regional economic development organization with the goals of creating jobs, strengthening, and supporting existing business, and increasing wealth and prosperity of the region. TVGA is a private/public consortium funded by the nine sectors of the region with membership from large employers, small businesses, utilities, educational institutions, non‐profits, city government, county government, financial institutions, and developers/real estate/contractors. Our region consists of Flagstaff, Winslow, Sedona and Camp Verde and all of Coconino County.

MISSION: “With our partners, we provide quality economic growth for Northern Arizona.”

PROJECT & DESCRIPTION: We are hoping to revitalize and strengthen our brand, creating a cohesive and impactful identity that resonates with our target audience. Utilization of recent strategic data should be incorporated to invoke personal, emotional, and genuine elements into promotional activities, ensuring that marketing strategies resonate on a human level rather than feeling impersonal or automated. Collaborating with our team to understand key messaging is imperative. Communicating who we are, what we do and why it’s important is key.
WEBSITE: Update the existing website for a comprehensive refresh. Our goal is to enhance the user experience, modernize the design and improve functionality to better align with our brand and goals outlined in the strategic plan.
The website should do the following:
• Engage website visitors with fresh and updated content.
• Capture website visitors and convert them into a lead.
• Refresh current website with more photo rich content.
• Create a page that shows available buildings or land options.
• Create a search function.
• Ensure mobile friendliness.
• Ensure that the website is user friendly.
Create a feature that allows us to upload properties in the region for sale or lease.

Please see the attached new logo which has yet to be launched as we want to roll it out with the website refresh. We are open to other features that you feel our website should have. Please also see our attached strategic roadmap.

```html
<!DOCTYPE html>
<html lang="en">
<head>
<meta charset="utf-8">
<title>TVGA — Tolvane Valley Growth Alliance</title>
<link rel="stylesheet" href="https://fonts.googleapis.com/css2?family=Manrope:wght@600;700;800&family=Inter:wght@400;500;600&display=swap">
<style>
:root{
  --navy:#0d3b73;
  --deep:#06326b;
  --panel:#1b4a84;
  --orange:#e05a0c;
  --ink:#1d2733;
  --muted:#6b7684;
  --soft:#f4f6f9;
  --line:#d9dee5;
  --foot:#2d3b4e;
  --white:#ffffff;
}
*{box-sizing:border-box;margin:0;padding:0}
html,body{width:1200px;height:1200px;overflow:hidden;background:var(--white)}
body{font-family:Inter,sans-serif;color:var(--ink)}
.page{position:absolute;left:434.8px;top:0;width:532px;height:1932px;transform:scale(0.62112);transform-origin:0 0;background:var(--soft);overflow:hidden}
.abs{position:absolute}
.h{font-family:Manrope,sans-serif;font-weight:800;color:var(--navy);letter-spacing:-0.2px}
.hero{left:0;top:0;width:532px;height:259px;background:linear-gradient(180deg,#262c3d 0%,#3c3a4e 25%,#8a4a3c 42%,#c86a3e 50%,#5b4b59 60%,#2b3445 75%,#151c26 100%)}
.logo{font-family:Manrope,sans-serif;font-weight:800;font-size:9px;color:var(--white);display:flex;align-items:center;gap:3px}
.logo i{width:5px;height:5px;background:var(--white);display:block}
.nav a{position:absolute;top:10px;font-size:5px;font-weight:600;color:var(--white);text-decoration:none}
.invest{left:430px;top:8px;width:28px;height:10px;border-radius:5px;background:var(--orange);color:var(--white);font-size:4.5px;font-weight:600;display:flex;align-items:center;justify-content:center}
.hero-title{left:0;width:532px;top:94px;text-align:center;font-family:Manrope,sans-serif;font-weight:700;font-size:24px;line-height:28px;color:var(--white)}
.hero-sub{left:146px;width:240px;top:156px;text-align:center;font-size:6.3px;line-height:11px;color:var(--white)}
.mission{left:0;top:259px;width:532px;height:206px;background:var(--white)}
.eyebrow{font-size:4.6px;font-weight:600;color:var(--orange);letter-spacing:.2px}
.mission-title{left:79px;top:292px;width:190px;font-size:14px;line-height:17.4px}
.body{font-size:4.9px;line-height:9px;color:var(--muted)}
.stat{width:71px;height:54px;background:var(--white);border-radius:3px;box-shadow:0 2px 8px rgba(13,59,115,.12);text-align:center}
.stat b{display:block;margin-top:14px;font-family:Manrope,sans-serif;font-weight:700;font-size:12.5px;color:var(--orange)}
.stat span{display:block;margin-top:6px;font-size:4.3px;color:var(--muted)}
.sec-title{left:0;width:532px;text-align:center;font-size:14px;line-height:17px}
.center{left:0;width:532px;text-align:center}
.card{background:var(--white);border-radius:3px;box-shadow:0 2px 8px rgba(13,59,115,.10);overflow:hidden}
.sector{top:573px;width:119px;height:189px}
.sector .ph{height:82px}
.sector h3{font-family:Manrope,sans-serif;font-weight:700;font-size:8.6px;line-height:11px;color:var(--navy);margin:11px 10px 6px}
.sector p{margin:0 10px;font-size:4.9px;line-height:9px;color:var(--muted)}
.more{font-size:4.8px;font-weight:600;color:var(--orange)}
.sector .more{position:absolute;left:10px;top:171px}
.life{left:79px;top:812px;width:167px;height:216px}
.checks{list-style:none}
.checks li{position:relative;padding-left:14px;font-size:5.3px;line-height:10px;color:var(--ink);margin-bottom:6px}
.checks li::before{content:"";position:absolute;left:0;top:2px;width:7px;height:7px;border-radius:50%;background:var(--orange)}
.checks li::after{content:"";position:absolute;left:2.2px;top:4px;width:2.4px;height:1.3px;border-left:1px solid #fff;border-bottom:1px solid #fff;transform:rotate(-45deg)}
.spaces{left:0;top:1060px;width:532px;height:399px;background:var(--deep)}
.search{left:79px;top:1179px;width:379px;height:45px;border-radius:4px;background:var(--panel)}
.lbl{font-size:4.6px;font-weight:600;color:var(--white)}
.field{height:14px;border:1px solid #5c7ea8;border-radius:2px;background:#0f3c74;font-size:4.2px;color:var(--white);padding:4px 5px;display:flex;justify-content:space-between}
.btn{background:var(--orange);color:var(--white);font-weight:600;display:flex;align-items:center;justify-content:center;border-radius:8px}
.prop{top:1240px;width:119px;height:156px}
.prop .ph{margin:5px 5px 0;height:60px;background:linear-gradient(180deg,#d8dcdf,#bfc8cb)}
.prop h4{font-family:Manrope,sans-serif;font-weight:700;font-size:6.6px;color:var(--navy);margin:15px 8px 4px}
.pin{display:flex;align-items:center;gap:4px;margin:0 8px;font-size:4.6px;color:var(--muted)}
.prop p{margin:6px 8px 0;font-size:4.4px;line-height:7px;color:#eef0f3}
.prop .more{position:absolute;left:8px;top:141px;font-weight:500}
.contact{left:0;top:1459px;width:532px;height:309px;background:var(--white)}
.form{left:138px;top:1490px;width:262px;height:258px}
.input{position:absolute;left:21px;width:219px;height:16px;border:1px solid #c5ccd5;border-radius:2px;font-size:4.8px;color:var(--muted);padding:5px 5px}
.footer{left:0;top:1768px;width:532px;height:164px;background:var(--foot)}
.fh{font-size:5.2px;font-weight:600;color:var(--white)}
.fl{font-size:4.8px;line-height:12.7px;color:#cdd4dd}
.soc{width:12px;height:12px;border:1px solid #8a96a6;border-radius:50%}
</style>
</head>
<body>
<div class="page">

  <div class="abs hero" role="img" aria-label="Sunset sky over forested mountain ridges"></div>
  <div class="abs logo" style="left:80px;top:7px"><i></i>TVGA</div>
  <nav class="nav">
    <a style="left:248px">About Us</a>
    <a style="left:284px">Key Sectors</a>
    <a style="left:327px">Our Region</a>
    <a style="left:368px">Available Properties</a>
  </nav>
  <div class="abs invest">Invest Here</div>
  <h1 class="abs hero-title">Forging the Future of<br>Northern Arizona</h1>
  <p class="abs hero-sub">Uniting public and private leaders to cultivate a diverse, sustainable, and prosperous economy for all.</p>

  <section class="abs mission"></section>
  <svg class="abs" style="left:0;top:420px" width="532" height="50" viewBox="0 0 532 50"><path d="M0 5 Q266 90 532 5 L532 50 L0 50 Z" fill="#f4f6f9"/></svg>
  <div class="abs eyebrow" style="left:79px;top:281px">OUR MISSION</div>
  <h2 class="abs h mission-title">With Our Partners, We Provide Quality Economic Growth For Northern Arizona.</h2>
  <p class="abs body" style="left:79px;top:365px;width:182px">The Tolvane Valley Growth Alliance (TVGA) is a 501(c)(3) nonprofit organization dedicated to the regional prosperity of Coconino County. By fostering collaboration between business, government, and education, we work to create quality jobs, strengthen existing industries, and attract new investment to our vibrant communities.</p>
  <div class="abs stat" style="left:306px;top:301px"><b>4</b><span>Key Communities</span></div>
  <div class="abs stat" style="left:388px;top:301px"><b>9</b><span>Economic Sectors</span></div>
  <div class="abs stat" style="left:306px;top:366px"><b>150K+</b><span>Regional Population</span></div>
  <div class="abs stat" style="left:388px;top:366px"><b>6,000+</b><span>Square Miles</span></div>

  <h2 class="abs h sec-title" style="top:499px">A Landscape of Opportunity</h2>
  <p class="abs body center" style="top:521px;left:161px;width:210px">Northern Arizona's diverse economy is primed for growth in key sectors, driven by a talented workforce, robust infrastructure, and a world-class university.</p>

  <article class="abs card sector" style="left:79px">
    <div class="ph" role="img" aria-label="Researcher in a lab with red rock views" style="background:linear-gradient(180deg,#5f87a3,#9a6a55 60%,#3e4d58)"></div>
    <h3>Biomedical &amp;<br>Healthcare</h3>
    <p>A burgeoning hub for research, development, and healthcare technology, anchored by major institutions and a thriving culture of innovation.</p>
    <span class="more">Explore This Sector →</span>
  </article>
  <article class="abs card sector" style="left:209px">
    <div class="ph" role="img" aria-label="Distribution center with freight rail at sunrise" style="background:linear-gradient(180deg,#b9c3cc,#c39a6c 55%,#5a4a3c)"></div>
    <h3>Manufacturing &amp;<br>Logistics</h3>
    <p>Leverage strategic access to major interstate highways and rail lines connecting you to markets across the Southwest and beyond.</p>
    <span class="more">Explore This Sector →</span>
  </article>
  <article class="abs card sector" style="left:339px">
    <div class="ph" role="img" aria-label="Professionals meeting outside a brick building" style="background:linear-gradient(180deg,#6b4a3a,#4a4040 55%,#2d3038)"></div>
    <h3>Professional Services<br>&amp; Tech</h3>
    <p>Tap into a growing pool of educated talent from Tolvane State University and a community that supports remote work and modern business.</p>
    <span class="more">Explore This Sector →</span>
  </article>

  <div class="abs card life"></div>
  <div class="abs" role="img" aria-label="Family sharing a meal at an outdoor café in a small town" style="left:236px;top:860px;width:221px;height:120px;border-radius:3px;background:linear-gradient(160deg,#5d7a3e,#8a6a4a 50%,#4b4036)"></div>
  <div class="abs" style="left:94px;top:829px;font-size:4.6px;font-weight:500;color:var(--ink)">AN UNBEATABLE LIFESTYLE</div>
  <h2 class="abs h" style="left:94px;top:837px;width:130px;font-size:14px;line-height:17.4px">Build Your Business. Love Your Life.</h2>
  <p class="abs body" style="left:94px;top:893px;width:138px">Discover a place where career ambition and quality of life are not mutually exclusive. Northern Arizona offers a unique blend of vibrant communities, stunning natural beauty, and endless recreational opportunities.</p>
  <ul class="abs checks" style="left:95px;top:934px;width:138px">
    <li>World-class outdoor recreation, from hiking and skiing to exploring national parks.</li>
    <li>A rich tapestry of arts, culture, and history in our welcoming towns and cities.</li>
    <li>Access to top-tier education and a strong sense of community.</li>
  </ul>

  <section class="abs spaces"></section>
  <h2 class="abs h sec-title" style="top:1092px;color:var(--white);left:156px;width:220px">Find Your Space in Northern Arizona</h2>
  <p class="abs center" style="top:1131px;left:151px;width:230px;font-size:5.1px;line-height:9px;color:var(--white)">Explore available commercial and industrial properties for sale or lease across our region. Your next business location awaits. (Note: This is a front-end demonstration of the requested feature.)</p>
  <div class="abs search"></div>
  <div class="abs lbl" style="left:89px;top:1190px">Community</div>
  <div class="abs lbl" style="left:181px;top:1190px">Property Type</div>
  <div class="abs lbl" style="left:272px;top:1190px">Min. Size (sq. ft.)</div>
  <div class="abs field" style="left:89px;top:1200px;width:84px"><span>All Communities</span><span>⌄</span></div>
  <div class="abs field" style="left:181px;top:1200px;width:84px"><span>All Types</span><span>⌄</span></div>
  <div class="abs field" style="left:272px;top:1200px;width:84px;color:#7d95b4"><span>e.g. 5000</span></div>
  <div class="abs btn" style="left:364px;top:1202px;width:84px;height:12px;font-size:4.8px">Search</div>

  <article class="abs card prop" style="left:79px">
    <div class="ph" role="img" aria-label="Rendering of an industrial warehouse"></div>
    <h4>Prime Industrial Warehouse</h4>
    <div class="pin"><svg width="5" height="6" viewBox="0 0 10 12"><path d="M5 0a4 4 0 0 1 4 4c0 3-4 8-4 8S1 7 1 4a4 4 0 0 1 4-4z" fill="#6b7684"/><circle cx="5" cy="4" r="1.5" fill="#fff"/></svg>Flagstaff</div>
    <p>Large distribution building near the interstate with dock doors and rail access.</p>
    <span class="more">View Details</span>
  </article>
  <article class="abs card prop" style="left:209px">
    <div class="ph" role="img" aria-label="Rendering of a glass office building"></div>
    <h4>Modern Office Space</h4>
    <div class="pin"><svg width="5" height="6" viewBox="0 0 10 12"><path d="M5 0a4 4 0 0 1 4 4c0 3-4 8-4 8S1 7 1 4a4 4 0 0 1 4-4z" fill="#6b7684"/><circle cx="5" cy="4" r="1.5" fill="#fff"/></svg>Sedona</div>
    <p>Flexible class A suites with open floor plans and scenic views nearby.</p>
    <span class="more">View Details</span>
  </article>
  <article class="abs card prop" style="left:339px">
    <div class="ph" role="img" aria-label="Aerial rendering of a development site"></div>
    <h4>Commercial Development Land</h4>
    <div class="pin"><svg width="5" height="6" viewBox="0 0 10 12"><path d="M5 0a4 4 0 0 1 4 4c0 3-4 8-4 8S1 7 1 4a4 4 0 0 1 4-4z" fill="#6b7684"/><circle cx="5" cy="4" r="1.5" fill="#fff"/></svg>Camp Verde</div>
    <p>Shovel-ready acreage zoned for mixed commercial use with utilities in place.</p>
    <span class="more">View Details</span>
  </article>

  <section class="abs contact"></section>
  <div class="abs card form"></div>
  <h2 class="abs h sec-title" style="top:1512px;left:156px;width:220px">Ready to Build Your Future in Northern Arizona?</h2>
  <p class="abs body center" style="top:1551px;left:156px;width:220px">Contact us today to learn more about investment opportunities, site selection, and how TVGA can help your business thrive.</p>
  <div class="input" style="left:159px;top:1575px">Your Name</div>
  <div class="input" style="left:159px;top:1600px">Email Address</div>
  <div class="input" style="left:159px;top:1626px">Company (Optional)</div>
  <div class="input" style="left:159px;top:1651px;height:48px">How can we help?</div>
  <div class="abs btn" style="left:159px;top:1710px;width:219px;height:16px;font-size:5.2px">Send Inquiry</div>

  <footer class="abs footer"></footer>
  <div class="abs logo" style="left:79px;top:1822px;font-size:8px"><i></i>TVGA</div>
  <p class="abs" style="left:79px;top:1839px;width:134px;font-size:4.8px;line-height:9px;color:#6f7d90">The Tolvane Valley Growth Alliance is a private/public consortium strengthening the region through quality economic growth.</p>
  <div class="abs soc" style="left:79px;top:1874px"></div>
  <div class="abs soc" style="left:97px;top:1874px"></div>
  <div class="abs soc" style="left:115px;top:1874px"></div>
  <div class="abs fh" style="left:227px;top:1822px">Navigate</div>
  <div class="abs fl" style="left:227px;top:1834px">About Us<br>Key Sectors<br>Our Region<br>Available Properties</div>
  <div class="abs fh" style="left:309px;top:1822px">Resources</div>
  <div class="abs fl" style="left:309px;top:1834px">Strategic Roadmap<br>Investor Information<br>News &amp; Updates<br>Data Center</div>
  <div class="abs fh" style="left:391px;top:1822px">Contact</div>
  <div class="abs fl" style="left:391px;top:1834px;line-height:9px">TVGA Office<br>Northern Arizona</div>
  <div class="abs fl" style="left:391px;top:1856px">(555) 014-2290<br>info@tvga-tl.com</div>
  <div class="abs center" style="top:1915px;font-size:4.4px;color:#cdd4dd">© 2024 Tolvane Valley Growth Alliance. All Rights Reserved.</div>

</div>
</body>
</html>
```